Responsive Mobile Quorvo Jewelry Template

We need to adapt an existing Quorvo template to be 100% responsive and mobile friendly. Due to Quorvo rules, the template would need to be implemented only using HTML and CSS (no Javascript). The template design files and HTML/CSS files are required for this project. We prefer that it is implemented using a responsive framework such as Bootstrap.

An example of our current template can be found here (diamond only):
https://www.quorvo.example/itm/518203746291?ViewItem=&item=518203746291

And example of our template with an additional section for gemstone:
https://www.quorvo.example/itm/518203746837?ViewItem=&item=518203746837

We had also somewhat recently designed our Quorvo store landing page so some consistency with this would be desired:
http://www.quorvoshops.example/HalvrenDesignsLA

Please also refer to our website: https://halvrendesignsla.example/

Target Market(s)

Primarily women shopping for jewelry on Quorvo.

Industry/Entity Type

Jewelry

Coding

Coded - Design and coding required

Number of Pages Required

1 page

Font styles to use
Sans Serif

Requirements
Must have
• * A color scheme that fits with the existing template design.
• * REMOVE the product photo in the template.
• * Sections required for Description, Basic Details, and Diamond/Gemstone Details.
• * Please refer to https://pages.quorvo.example/sell/itemdescription/mobilefriendlyguidelines.html in particular, the template must use
Nice to have
• * Menu of links to other categories is desired in a mobile friendly way.
• * We are open to graphics for links to popular categories similar to those found on the store page.
• * Implemented using a standardized responsive framework such as Bootstrap.

```html
<!DOCTYPE html>
<html lang="en">
<head>
<meta charset="utf-8">
<title>Halvren Designs – Item Listing</title>
<link href="https://fonts.googleapis.com/css2?family=Montserrat:wght@400;500;600&family=Open+Sans:wght@400;600&display=swap" rel="stylesheet">
<style>
:root{
  --purple:#9a7ab5;
  --purple-light:#b49bcb;
  --purple-dark:#8a68a7;
  --ink:#222;
  --text:#444;
  --muted:#666;
  --panel:#f4f4f6;
  --line:#dcdcdc;
  --white:#fff;
}
*{box-sizing:border-box;margin:0;padding:0}
html,body{width:823px;height:1200px;overflow:hidden;background:var(--white)}
body{position:relative;font-family:"Open Sans",sans-serif;color:var(--text)}

.site-header .brand{position:absolute;left:77px;top:28px;display:flex;align-items:center;gap:8px}
.brand-mark{width:22px;height:22px;background:var(--purple-light)}
.brand-name{font-family:"Montserrat",sans-serif;font-size:17px;font-weight:500;color:var(--purple);letter-spacing:.5px}
.main-nav{position:absolute;right:74px;top:38px;display:flex;gap:22px}
.main-nav a{font-family:"Montserrat",sans-serif;font-size:11px;font-weight:500;color:#333;text-decoration:none}

.category-menu{position:absolute;left:77px;top:91px;width:170px;height:321px;border:1px solid var(--line)}
.category-menu .menu-title{background:var(--purple-light);color:#fff;font-size:8.5px;font-weight:600;text-align:center;line-height:14px;padding:5px 8px;height:37px}
.category-menu ul{list-style:none;padding:0 6px}
.category-menu li{height:31px;display:flex;align-items:center;gap:10px;font-size:8.2px;color:#333;border-bottom:1px solid #e6e6e6;padding-left:6px;white-space:nowrap}
.category-menu li:last-child{border-bottom:none}
.category-menu li svg{width:12px;height:12px;flex:none}

.panel{position:absolute;background:var(--panel);border:1px solid var(--line)}
.panel h2{font-family:"Montserrat",sans-serif;font-size:11px;font-weight:500;color:var(--ink);margin-bottom:8px}
.panel-description{left:258px;top:91px;width:239px;height:106px;padding:22px 19px}
.panel-description p{font-size:8px;line-height:15.5px;color:var(--text)}
.panel-details{left:258px;top:203px;width:239px;height:209px;padding:22px 19px}
.panel-diamond{left:506px;top:94px;width:238px;height:245px;padding:22px 19px}
.spec-table{border-collapse:collapse}
.spec-table th{font-size:8px;font-weight:600;color:#333;text-align:left;padding:0 0 0 2px;height:25.3px;vertical-align:middle;white-space:nowrap}
.spec-table td{font-size:8px;color:var(--text);height:25.3px;vertical-align:middle;white-space:nowrap}
.panel-details .spec-table th{width:76px}
.panel-diamond .spec-table th{width:94px;height:27.6px}
.panel-diamond .spec-table td{height:27.6px}

.natural-note{position:absolute;left:506px;top:356px;font-size:8px;color:#333}
.more-link{position:absolute;left:506px;top:377px;font-size:8px;font-weight:600;color:var(--purple);text-decoration:underline}
.more-text{position:absolute;left:506px;top:397px;font-size:9px;font-weight:600;color:var(--ink)}

.question-band{position:absolute;left:0;top:466px;width:823px;height:116px;background:linear-gradient(100deg,var(--purple-dark),var(--purple-light))}
.question-band h3{position:absolute;left:126px;top:33px;font-family:"Montserrat",sans-serif;font-weight:500;font-size:20px;line-height:27px;color:#fff}
.email-form{position:absolute;left:350px;top:40px;width:347px;height:36px;background:#fff;display:flex;align-items:center}
.email-form svg{margin-left:17px;width:10px;height:10px}
.email-form span{margin-left:9px;font-size:8.5px;color:#444;flex:1}
.email-form .send{width:106px;height:32px;margin-right:2px;background:var(--purple-light);color:#fff;font-family:"Montserrat",sans-serif;font-weight:600;font-size:11px;display:flex;align-items:center;justify-content:center}

.about-title{position:absolute;left:0;width:823px;top:626px;text-align:center;font-family:"Montserrat",sans-serif;font-weight:500;font-size:20px;color:var(--ink)}
.about-lead{position:absolute;left:0;width:823px;top:658px;text-align:center;font-size:8.5px;line-height:15px;color:var(--text)}

.policy-tabs{position:absolute;left:75px;top:707px;width:670px;height:298px;border:1px solid #cfcfcf}
.tab-bar{display:flex;align-items:center;height:50px;border-bottom:1px solid #cfcfcf}
.tab-bar div{font-family:"Montserrat",sans-serif;font-size:10.5px;font-weight:500;color:#444;padding:0 17px;white-space:nowrap}
.tab-bar .active{position:relative;background:var(--purple-light);color:#fff;height:50px;width:147px;display:flex;align-items:center;justify-content:center;padding:0}
.tab-bar .active::after{content:"";position:absolute;left:32px;bottom:-7px;border-left:5px solid transparent;border-right:5px solid transparent;border-top:7px solid var(--purple-light)}
.tab-bar .first{padding-left:21px}
.tab-body{padding:30px 31px}
.tab-body h4{font-family:"Montserrat",sans-serif;font-weight:500;font-size:11px;color:#333;margin-bottom:11px}
.tab-body h5{font-family:"Montserrat",sans-serif;font-weight:600;font-size:12.5px;color:#333;margin-bottom:6px}
.tab-body p{font-size:9.5px;line-height:21px;color:#333;margin-bottom:8px}

.trust-badges{position:absolute;top:1041px;left:0;width:823px}
.badge{position:absolute;width:78px;height:78px;border-radius:50%;border:1px solid #ddd;background:#fff;display:flex;align-items:center;justify-content:center}
.badge i{display:block;width:44px;height:44px;border-radius:50%;background:#d9d9e0}

.site-footer{position:absolute;left:0;top:1153px;width:823px;height:47px;background:linear-gradient(90deg,var(--purple-dark),var(--purple-light));color:#fff;font-size:8.5px;text-align:center;line-height:47px}
</style>
</head>
<body>
<header class="site-header">
  <div class="brand"><span class="brand-mark"></span><span class="brand-name">HALVREN DESIGNS</span></div>
  <nav class="main-nav"><a href="#">ABOUT US</a><a href="#">FAQS</a><a href="#">WHY BUY FROM US</a><a href="#">SAVE SELLER</a></nav>
</header>

<aside class="category-menu">
  <div class="menu-title">Please choose a category below to see more subcategories</div>
  <ul>
    <li><svg viewBox="0 0 12 12"><circle cx="6" cy="7" r="4" fill="none" stroke="#555" stroke-width="1.3"/></svg>Diamond Engagement Rings</li>
    <li><svg viewBox="0 0 12 12"><circle cx="6" cy="7" r="4" fill="none" stroke="#555" stroke-width="1.3"/></svg>Fancy Yellow &amp; Pink Diamond</li>
    <li><svg viewBox="0 0 12 12"><circle cx="6" cy="7" r="4" fill="none" stroke="#888" stroke-width="1.1"/></svg>Cocktail Fashion Diamond Rings</li>
    <li><svg viewBox="0 0 12 12"><circle cx="6" cy="7" r="4" fill="none" stroke="#888" stroke-width="1.1"/></svg>Semi Mount Diamond Rings</li>
    <li><svg viewBox="0 0 12 12"><circle cx="6" cy="7" r="4" fill="none" stroke="#888" stroke-width="1.1"/></svg>Men's Diamond Jewelry</li>
    <li><svg viewBox="0 0 12 12"><rect x="3" y="4" width="6" height="7" fill="#555"/></svg>Diamond Pendants</li>
    <li><svg viewBox="0 0 12 12"><line x1="3" y1="1" x2="3" y2="11" stroke="#555"/><line x1="9" y1="1" x2="9" y2="11" stroke="#555"/></svg>Diamond Earrings</li>
    <li><svg viewBox="0 0 12 12"><ellipse cx="6" cy="5" rx="5" ry="3" fill="none" stroke="#555"/></svg>Diamond Necklaces</li>
    <li><svg viewBox="0 0 12 12"><circle cx="6" cy="6.5" r="4.5" fill="none" stroke="#333" stroke-width="1.6"/></svg>Diamond Bracelets &amp; Bangles</li>
  </ul>
</aside>

<section class="panel panel-description">
  <h2>Item Description</h2>
  <p>Exquisite Oval Aquamarine Gemstone Surrounded By A Delicate Halo Of Diamonds Mounted In A Classic 14k Yellow Gold Setting</p>
</section>

<section class="panel panel-details">
  <h2>Item Details</h2>
  <table class="spec-table">
    <tr><th>Model Number:</th><td>HDL-FY40901AQC-600</td></tr>
    <tr><th>Metal:</th><td>14k Yellow Gold</td></tr>
    <tr><th>Weight:</th><td>4.08 grams</td></tr>
    <tr><th>L x W x H:</th><td>12 x 10 x 7.2 MM</td></tr>
    <tr><th>Style:</th><td>Halo</td></tr>
    <tr><th>Ring Size:</th><td>6 (contact us for sizing options)</td></tr>
  </table>
</section>

<section class="panel panel-diamond">
  <h2>Diamond Details</h2>
  <table class="spec-table">
    <tr><th>Total Carat Weight:</th><td>0.19 CT</td></tr>
    <tr><th>Diamond Count:</th><td>22</td></tr>
    <tr><th>Shape:</th><td>Round</td></tr>
    <tr><th>Color/Clarity:</th><td>G / SI1</td></tr>
    <tr><th>Other Shape:</th><td>Round</td></tr>
    <tr><th>Other Color/Clarity:</th><td>G / SI1</td></tr>
    <tr><th>Certificate:</th><td>VGL (click for more info)</td></tr>
  </table>
</section>

<p class="natural-note">All of our diamonds &amp; gemstones are 100% natural!</p>
<a class="more-link" href="#">Click Here</a>
<p class="more-text">To View Our Other Diamond Rings!</p>

<section class="question-band">
  <h3>ASK QUESTIONS<br>VIA EMAIL</h3>
  <div class="email-form">
    <svg viewBox="0 0 10 10"><rect x="0.5" y="1.5" width="9" height="7" fill="none" stroke="#444"/><polyline points="0.5,2 5,6 9.5,2" fill="none" stroke="#444"/></svg>
    <span>Enter Your Email</span>
    <div class="send">Send Now</div>
  </div>
</section>

<h2 class="about-title">ABOUT HALVREN DESIGNS</h2>
<p class="about-lead">Lorem ipsum dolor sit amet, consectetur adipiscing elit, sed do eiusmod tempor<br>incididuntut labore et dolore magna aliqua.</p>

<section class="policy-tabs">
  <div class="tab-bar">
    <div class="active">SHIPPING DETAILS</div>
    <div class="first">PRODUCT GUARANTEE</div>
    <div>RETURN POLICY</div>
    <div>PRIVACY POLICY</div>
    <div>WHY US</div>
  </div>
  <div class="tab-body">
    <h4>PARCELWING 2 DAY: FREE (U.S.A. ONLY)</h4>
    <h5>WE SHIP WORLDWIDE</h5>
    <p>International Buyers - Please Note: Import duties, taxes, and charges are not included in the item price or shipping cost. These charges are the buyer's responsibility. Please check with your country's customs office to determine what these additional costs will be prior to bidding or buying.</p>
    <p>All packages are fully insured and require signature confirmation. Once your item(s) are ready to leave our facility a shipping tracking number will be sent to you. Business days do not include Saturday, Sunday or holidays. Please be sure to inspect your package upon arrival for tampering or any damage. Rush orders are welcome. Please call for availability.</p>
  </div>
</section>

<div class="trust-badges">
  <div class="badge" style="left:205px" role="img" aria-label="Business accreditation badge"><i></i></div>
  <div class="badge" style="left:372px" role="img" aria-label="Gemological institute badge"><i></i></div>
  <div class="badge" style="left:539px" role="img" aria-label="Gemological laboratory badge"><i></i></div>
</div>

<footer class="site-footer">Copyrights © 2018. All Rights Reserved.</footer>
</body>
</html>
```